Asia based real estate financing firm needs and AWESOME design for a biz card -Harborline Lending Partners

Looking for a stylish, & corporate-looking business card for a real estate financing brokerage firm in Asia, offering global mortgage loans. I uploaded our current logos. We would like to add a splash of color (perhaps the house icon) or any other suggestions are open. For the winning designer, we have a lot of work! Thanks and best of luck!

Target Market(s)

Real estate investors globally. We want to look more like a BANK and NOT a real estate company. Please don't play up on a "house" design.

Industry/Entity Type

Banking

Contact Information for Business Card

Harborline Lending Partners
Peter Walsh
Co-Founder | Partner

42 Kelvin Street, Suite 310
Singapore 074219
www.hlp-lend.example
peterwalsh@hlp-lend.example
+65 555-0147
WeChat: peterwalsh

Colors

Designer to choose colors to be used in the design.

Requirements
Must have
• Must have the standard business requirements for a card; name, address, email, etc
• Can be horizontal or vertical.
Nice to have
• It would be great to see some sort of variation to the logo with a pop of color. Red is good as we're in Asia, however, other options work as well.
• Our tag line is - Lending Without Limits. It doesn't have to be on the card but might be nice.
• I'd like to start seeing our tagline within the cards as well. - Lending Without Limits.
• Also, please add our location. The location for this card is Singapore so perhaps it can be highlighted or emphasised in some way.
• Singapore | Hong Kong | Shanghai | Manila
• As we will soon open an office in Shanghai, having an option for both languages would be great.
Should not have
• I'm exceited and open to your creativity ... knock it out of the park!

```html
<!DOCTYPE html>
<html lang="en">
<head>
<meta charset="utf-8">
<title>Harborline Lending Partners — Business Card</title>
<link rel="stylesheet" href="https://fonts.googleapis.com/css2?family=Cinzel:wght@500&family=Arimo:wght@400&display=swap">
<style>
  :root {
    --brand-red: #e5202e;
    --ink: #141414;
    --paper: #ffffff;
    --backdrop: #ebe8e4;
    --serif: "Cinzel", "Times New Roman", serif;
    --sans: "Arimo", Arial, sans-serif;
  }
  * { box-sizing: border-box; margin: 0; padding: 0; }
  html, body { width: 1200px; height: 1200px; overflow: hidden; }
  body {
    background: var(--backdrop);
    display: flex;
    flex-direction: column;
    align-items: center;
    justify-content: center;
    gap: 56px;
  }
  .card {
    position: relative;
    width: 900px;
    height: 514px;
    overflow: hidden;
    box-shadow: 0 6px 18px rgba(0,0,0,0.18);
  }

  /* Back face */
  .card-back {
    background: var(--brand-red);
    display: flex;
    flex-direction: column;
    align-items: center;
    justify-content: center;
    gap: 22px;
    color: var(--paper);
  }
  .card-back .brand-name {
    font-family: var(--serif);
    font-weight: 500;
    font-size: 46px;
    letter-spacing: 1px;
  }
  .card-back .tagline {
    font-family: var(--serif);
    font-weight: 500;
    font-size: 22px;
    letter-spacing: 4px;
    text-transform: uppercase;
  }

  /* Front face */
  .card-front { background: var(--paper); }
  .contact-panel {
    position: absolute;
    left: 500px;
    top: 244px;
    right: 0;
    bottom: 0;
    background: var(--brand-red);
    border-top: 6px solid var(--ink);
  }
  .base-rule {
    position: absolute;
    left: 0;
    right: 400px;
    bottom: 0;
    height: 14px;
    background: var(--ink);
  }
  .card-front .brand-name {
    position: absolute;
    right: 40px;
    top: 70px;
    font-family: var(--serif);
    font-weight: 500;
    font-size: 26px;
    color: var(--brand-red);
  }
  .holder {
    position: absolute;
    left: 60px;
    top: 262px;
    font-family: var(--sans);
  }
  .holder-name {
    font-family: var(--serif);
    font-weight: 500;
    font-size: 30px;
    color: var(--brand-red);
    font-variant: small-caps;
    line-height: 1.1;
  }
  .holder-role {
    font-size: 24px;
    color: var(--ink);
    margin-top: 4px;
  }
  .address {
    position: absolute;
    left: 60px;
    top: 370px;
    font-family: var(--sans);
    font-style: normal;
    font-size: 21px;
    line-height: 30px;
    color: var(--ink);
  }
  .contact-list {
    position: absolute;
    right: 38px;
    top: 290px;
    list-style: none;
    font-family: var(--sans);
    font-size: 19px;
    line-height: 35px;
    color: var(--paper);
    text-align: right;
  }
  .contact-list li {
    display: flex;
    align-items: center;
    justify-content: flex-end;
    gap: 10px;
  }
  .contact-list svg { width: 17px; height: 17px; flex: none; }
</style>
</head>
<body>

  <section class="card card-back" aria-label="Business card, back">
    <div class="brand-name">Harborline Lending Partners</div>
    <div class="tagline">Lending Without Limits</div>
  </section>

  <section class="card card-front" aria-label="Business card, front">
    <div class="contact-panel" aria-hidden="true"></div>
    <div class="base-rule" aria-hidden="true"></div>

    <div class="brand-name">Harborline Lending Partners</div>

    <div class="holder">
      <div class="holder-name">Peter Walsh</div>
      <div class="holder-role">Co-Founder | Partner</div>
    </div>

    <address class="address">
      42 Kelvin Street, Suite 310<br>
      Singapore 074219
    </address>

    <ul class="contact-list">
      <li>+65 555-0147
        <svg viewBox="0 0 24 24" aria-hidden="true"><path fill="#fff" d="M6.6 10.8a15 15 0 0 0 6.6 6.6l2.2-2.2a1 1 0 0 1 1-.25 11.4 11.4 0 0 0 3.6.57 1 1 0 0 1 1 1V20a1 1 0 0 1-1 1A17 17 0 0 1 3 4a1 1 0 0 1 1-1h3.5a1 1 0 0 1 1 1c0 1.25.2 2.45.57 3.57a1 1 0 0 1-.25 1z"/></svg>
      </li>
      <li>peterwalsh@hlp-lend.example
        <svg viewBox="0 0 24 24" aria-hidden="true"><rect x="2" y="5" width="20" height="14" rx="1.5" fill="#fff"/><path d="M3 6l9 7 9-7" fill="none" stroke="#e5202e" stroke-width="1.6"/></svg>
      </li>
      <li>www.hlp-lend.example
        <svg viewBox="0 0 24 24" aria-hidden="true"><g fill="none" stroke="#fff" stroke-width="1.8"><circle cx="12" cy="12" r="9"/><ellipse cx="12" cy="12" rx="4" ry="9"/><path d="M3 12h18"/></g></svg>
      </li>
      <li>peterwalsh
        <svg viewBox="0 0 24 24" aria-hidden="true"><g fill="none" stroke="#fff" stroke-width="1.8"><path d="M9.5 4C5.4 4 2.5 6.6 2.5 9.7c0 1.8 1 3.3 2.5 4.4L4.4 16.5l2.8-1.4c.7.2 1.5.3 2.3.3"/><path d="M15 9c-3.6 0-6.5 2.3-6.5 5.1s2.9 5.1 6.5 5.1c.7 0 1.3-.1 1.9-.3l2.4 1.2-.5-2.1c1.4-.9 2.2-2.3 2.2-3.9C21.5 11.3 18.6 9 15 9z"/></g></svg>
      </li>
    </ul>
  </section>

</body>
</html>
```